Elegant and modern Wedding Photography brochure

My existing brochure (attached) needs a major facelift. This is one of the main selling tools - it gets emailed to my clients when they make an equiry on what packages i offer and it is printed out and walked through at our first meeting. This brochure is as critical as my website - it needs to sing!

I'm looking for an eye-catching design that says:
Elegant
Modern
Clean
Crisp
Not cutesy or lovey-dovey thanks - we are more sophisticated and professional than that.

Update images to some of the latest weddings I've shot also. Let me know files and resolution you need. I've enabled right-click to download images on my site for a limited time. Please note that I retain copyright and will pursue any breeches.

Http://www.carlathornbey.com/Melbourne-wedding-photography
Updates

Thanks for all of your designs! Will take a few days to decide.

Target Market(s)

Australian Women aged 24-44

Industry/Entity Type

Wedding

Font styles to use
Other font styles liked:
• Century Gothic

Requirements
Must have
• Easy to print - does not have to be 6 A4 pages like the existing brochure
Nice to have
• Some full page images - The photos are supposed to be the hero here :-)
Should not have
• Not cutesy or lovey-dovey thanks - we are more sophisticated and professional than that.

No black backgrounds, I prefer a white thanks

No images in organic shaped boxes (like the rectangles in the logo - no thanks).
Keep the lines straight and sharp

```html
<!DOCTYPE html>
<html lang="en">
<head>
<meta charset="utf-8">
<title>Carla's approach – Wedding Photography Brochure</title>
<link rel="stylesheet" href="https://fonts.googleapis.com/css2?family=Questrial&display=swap">
<style>
  :root {
    --page-bg: #ffffff;
    --panel-top: #261733;
    --panel-bottom: #390b5c;
    --accent-purple: #9a1fe0;
    --body-ink: #1a1a1a;
    --panel-ink: #e6dcef;
    --photo-sky: #cfe9e2;
    --photo-deep: #3a3f44;
  }
  * { margin: 0; padding: 0; box-sizing: border-box; }
  html, body {
    width: 1200px; height: 1000px; overflow: hidden;
    background: var(--page-bg);
  }
  .brochure-page {
    position: relative; width: 1200px; height: 1000px;
    font-family: "Questrial", "Century Gothic", sans-serif;
    color: var(--body-ink);
  }
  .side-panel {
    position: absolute; left: 158px; top: 178px; width: 354px; height: 642px;
    background: linear-gradient(180deg, var(--panel-top) 0%, var(--panel-bottom) 100%);
  }
  .hero-photo {
    position: absolute; left: 200px; top: 255px; width: 471px; height: 313px;
    background: linear-gradient(180deg, var(--photo-sky) 0%, #a9c7c4 45%, var(--photo-deep) 100%);
  }
  .page-title {
    position: absolute; right: 163px; top: 196px;
    font-size: 45px; font-weight: 400; letter-spacing: 3px;
    color: var(--accent-purple); white-space: nowrap;
  }
  .page-subtitle {
    position: absolute; right: 163px; top: 254px;
    font-size: 21px; font-weight: 400; letter-spacing: 1.6px;
    color: #111; white-space: nowrap;
  }
  .info-block { position: absolute; }
  .info-block h2 {
    font-size: 16.5px; font-weight: 400; letter-spacing: 1.2px;
    color: var(--accent-purple); margin-bottom: 14px;
  }
  .info-block p {
    font-size: 11.3px; line-height: 15px; letter-spacing: 0.9px;
    text-align: justify;
  }
  .block-formal { left: 688px; top: 397px; width: 352px; }
  .block-formal h2 { margin-bottom: 15px; }
  .block-style { left: 206px; top: 602px; width: 264px; }
  .block-style h2 { color: #ffffff; }
  .block-style p { color: var(--panel-ink); }
  .block-presentation { left: 531px; top: 609px; width: 240px; }
  .block-season { left: 800px; top: 609px; width: 241px; }
</style>
</head>
<body>
<main class="brochure-page">
  <div class="side-panel"></div>
  <div class="hero-photo" role="img" aria-label="Bridal party posing on a seaside jetty: groomsmen in dark suits, the couple kissing, bridesmaids in navy dresses, a young page boy reclining in front"></div>

  <h1 class="page-title">Carla’s approach</h1>
  <p class="page-subtitle">Enjoy your special day!</p>

  <section class="info-block block-formal">
    <h2>Formal Photography</h2>
    <p>Many of Carla’s clients book her because of the easy-going approach she has. They can get on with having a great time on their day without worrying about formal photography. However, there are occasions when clients do want formal family pictures, and Carla is more than happy to accommodate their requests. In order to keep the disruption on the day to a minimum, we recommend that Carla photographs no more than 6 groups, and a select number of the special couple.</p>
  </section>

  <section class="info-block block-style">
    <h2>Style &amp; Approach</h2>
    <p>Carla can observe and capture your wedding day in the background, quickly and quietly taking photojournalistic pictures rather than directing it if you prefer. Or she can confidently play the role of Art Director and instruct beautiful poses. Either way, what is most important is that her clients are relaxed and having a really great time on their wedding day!</p>
  </section>

  <section class="info-block block-presentation">
    <h2>Image Presentation</h2>
    <p>The most professional way of presenting clients with their photographs is in an elegantly designed photo book. Carla’s clients only pay one fixed price for the photography, regardless of how many images taken. There are no hard sell procedures to go through, and the completed book is prepared within 2-6 weeks after the wedding day.</p>
  </section>

  <section class="info-block block-season">
    <h2>Time of Year</h2>
    <p>Signature pictures can be taken on overcast days or winter months. Don’t worry if the sky is not perfectly blue. In the end, regardless of the weather – it’s the timeless mood of the day that Carla strives to capture.</p>
  </section>
</main>
</body>
</html>
```